Pine Vale Accounting - New Postcard for B2B marketing

I need a postcard for my business that provides cloud-based bookkeeping services with LedgerCloud Online. Our clients are small independently owned businesses. Please use our website for inspiration (colors, content, etc)... www.PineValeAccounting.example.

Target Market(s)

Small, independently-owned businesses, including restaurants, retail stores, small medical practices, etc

Industry/Entity Type

Bookkeeper

Font styles to use
Serif

Colors
3276b5
155ea9
c4d6e9
85cae6
33a6d7

Requirements
Must have
• Must have my logo (see attached), business contact info (see website), description of services, blue color scheme
Nice to have
• Maybe add "Prices starting at $750/mo"
Content should match info on our website
4 x 6 horizontal postcard (see attached template)

```html
<!DOCTYPE html>
<html lang="en">
<head>
<meta charset="utf-8">
<title>Pine Vale Accounting – Postcard</title>
<link rel="stylesheet" href="https://fonts.googleapis.com/css2?family=Poppins:wght@400;500;600;700&family=Montserrat:wght@700;800&family=Oswald:wght@600&display=swap">
<style>
  :root{
    --navy:#1a3a6b;
    --navy-deep:#173561;
    --mid-blue:#0e6aa8;
    --bright-blue:#155ea9;
    --pale-blue:#c4d6e9;
    --brand-green:#2ca24a;
    --white:#ffffff;
    --ink:#111111;
    --backdrop:#cfcfcf;
    --photo-light:#e9e9e9;
    --photo-dark:#6d6d6d;
  }
  *{box-sizing:border-box;margin:0;padding:0}
  html,body{width:1034px;height:1200px;overflow:hidden}
  body{background:var(--backdrop);position:relative;font-family:"Poppins",sans-serif;color:var(--white)}
  .postcard{position:absolute;left:32px;width:796px;height:536px;background:var(--white);overflow:hidden}
  .postcard--front{top:39px}
  .postcard--back{top:626px}
  .postcard__art{position:absolute;inset:0;width:796px;height:536px}

  /* brand lockup */
  .brand{position:absolute;left:18px;top:22px;display:flex;align-items:center;gap:12px}
  .brand__mark{width:44px;height:44px;border-radius:50%;flex:none}
  .brand__name{font-family:"Poppins",sans-serif;font-weight:600;font-size:31px;line-height:1.05;letter-spacing:-0.3px}
  .postcard--front .brand__mark{background:var(--navy)}
  .postcard--front .brand__name{color:var(--navy)}
  .postcard--back .brand__mark{background:var(--white)}
  .postcard--back .brand__name{color:var(--white)}

  /* front: price block */
  .price{position:absolute;left:17px;top:422px}
  .price__label{font-size:19px;font-weight:500;line-height:1}
  .price__amount{font-family:"Oswald",sans-serif;font-weight:600;font-size:62px;line-height:1;margin-top:4px;letter-spacing:0.5px}

  /* front: services */
  .services{position:absolute;right:15px;top:0;width:400px;text-align:right}
  .services__title{position:absolute;right:0;top:12px;font-family:"Montserrat",sans-serif;font-weight:800;font-size:36px;line-height:1;white-space:nowrap}
  .service{position:absolute;right:0}
  .service__head{display:flex;justify-content:flex-end;align-items:flex-end;gap:6px}
  .service__name{font-size:18px;font-weight:600;line-height:1}
  .service__icon{width:28px;height:28px;flex:none}
  .service__text{margin-top:7px;font-size:10.6px;line-height:13px;text-transform:uppercase;margin-left:auto}
  .service--bookkeeping{top:86px}
  .service--bookkeeping .service__text{width:300px}
  .service--reporting{top:244px}
  .service--reporting .service__text{width:256px}
  .service--payroll{top:404px}
  .service--payroll .service__text{width:296px}

  /* back: message */
  .message{position:absolute;left:18px;top:136px;width:372px}
  .message__title{font-family:"Montserrat",sans-serif;font-weight:800;font-size:34px;line-height:43px;text-transform:uppercase}
  .message__lead{margin-top:4px;font-weight:600;font-size:13.6px;line-height:17.5px;text-transform:uppercase}
  .vision{margin-top:6px;width:318px}
  .vision__title{font-weight:700;font-size:13.5px;text-transform:uppercase;line-height:1.1}
  .vision__text{margin-top:4px;font-size:5.8px;line-height:7.9px;text-transform:uppercase}
  .vision__text + .vision__text{margin-top:3px}
  .contact{position:absolute;left:18px;top:422px}
  .contact__label{font-size:14px;font-weight:400;line-height:1}
  .contact__phone{display:flex;align-items:center;gap:3px;font-weight:600;font-size:33px;line-height:1;margin-top:4px;letter-spacing:-0.5px}
  .contact__phone svg{width:12px;height:24px}
  .contact__email{display:flex;align-items:center;gap:5px;font-size:10.5px;margin-top:5px}
  .contact__email svg{width:12px;height:9px}
  .social{position:absolute;left:238px;top:496px;display:flex;gap:9px}
  .social__dot{width:24px;height:24px;border-radius:50%;background:var(--white)}

  /* back: address side */
  .stamp-box{position:absolute;left:685px;top:19px;width:95px;height:106px;border:1.5px solid var(--ink)}
  .address-line{position:absolute;left:481px;width:300px;height:0;border-top:1.5px solid var(--ink)}
</style>
</head>
<body>

<!-- FRONT -->
<section class="postcard postcard--front" aria-label="Postcard front">
  <svg class="postcard__art" viewBox="0 0 796 536">
    <defs>
      <linearGradient id="photoTone" x1="0" y1="0" x2="0" y2="1">
        <stop offset="0" stop-color="var(--white)"/>
        <stop offset="0.35" stop-color="var(--photo-light)"/>
        <stop offset="1" stop-color="var(--photo-dark)"/>
      </linearGradient>
    </defs>
    <polygon role="img" aria-label="Black and white photo of a team of accountants reviewing documents together"
      points="0,160 350,160 398,300 318,536 0,536" fill="url(#photoTone)"/>
    <polygon points="354,0 796,0 796,536 347,536 414,330 414,300" fill="var(--navy)"/>
    <polygon points="399,207 796,207 796,384 410,384 414,330 414,300" fill="var(--mid-blue)"/>
    <polygon points="311,0 344,0 408,300 398,300" fill="var(--mid-blue)"/>
    <polygon points="344,0 356,0 414,300 408,300" fill="var(--white)"/>
    <polygon points="306,536 334,536 410,360 400,360" fill="var(--mid-blue)"/>
    <polygon points="334,536 348,536 416,360 410,360" fill="var(--white)"/>
    <circle cx="409" cy="328" r="63" fill="var(--white)"/>
    <circle cx="409" cy="328" r="56" fill="none" stroke="var(--navy)" stroke-width="1.5"/>
    <circle cx="409" cy="328" r="41" fill="var(--brand-green)"/>
    <polygon points="0,416 309,416 252,516 0,516" fill="var(--navy)" opacity="0.92"/>
  </svg>

  <div class="brand">
    <span class="brand__mark"></span>
    <span class="brand__name">Pine Vale<br>Accounting</span>
  </div>

  <div class="price">
    <p class="price__label">PRICES STARTING AT</p>
    <p class="price__amount">$750/MO</p>
  </div>

  <div class="services">
    <h2 class="services__title">SERVICE</h2>

    <article class="service service--bookkeeping">
      <div class="service__head">
        <h3 class="service__name">BOOKKEEPING</h3>
        <svg class="service__icon" viewBox="0 0 28 28" aria-hidden="true">
          <circle cx="14" cy="8" r="7" fill="var(--white)"/>
          <text x="14" y="11.5" text-anchor="middle" font-size="9" font-weight="700" fill="var(--navy)" font-family="Poppins, sans-serif">$</text>
          <ellipse cx="14" cy="18" rx="11" ry="3.2" fill="none" stroke="var(--white)" stroke-width="2"/>
          <ellipse cx="14" cy="23" rx="11" ry="3.2" fill="none" stroke="var(--white)" stroke-width="2"/>
        </svg>
      </div>
      <p class="service__text">Let us take over the day to day bookkeeping so you can get back to running your business. We offer LedgerCloud Online setup and ongoing bookkeeping, including daily journal entries, accounts payables &amp; receivables, bill pay, sales tax reporting &amp;</p>
    </article>

    <article class="service service--reporting">
      <div class="service__head">
        <h3 class="service__name">FINANCIAL REPORTING</h3>
        <svg class="service__icon" viewBox="0 0 28 28" aria-hidden="true" fill="none" stroke="var(--white)" stroke-width="1.4">
          <rect x="8" y="2" width="17" height="24"/>
          <line x1="11" y1="8" x2="22" y2="8"/>
          <line x1="11" y1="13" x2="22" y2="13"/>
          <line x1="11" y1="17" x2="22" y2="17"/>
          <line x1="11" y1="21" x2="22" y2="21"/>
          <rect x="2" y="11" width="5" height="6" fill="var(--white)"/>
        </svg>
      </div>
      <p class="service__text">We'll provide easy to understand financial reports that allow you and your team to manage cash flow, create budgets and make forecasting decisions. Want real time data? Let us provide solutions with the latest in mobile apps and dashboards.</p>
    </article>

    <article class="service service--payroll">
      <div class="service__head">
        <h3 class="service__name">FINANCIAL REPORTING</h3>
        <svg class="service__icon" viewBox="0 0 28 28" aria-hidden="true" fill="none" stroke="var(--white)" stroke-width="1.4">
          <circle cx="6" cy="5" r="2.5"/>
          <circle cx="14" cy="4" r="2.5"/>
          <circle cx="22" cy="5" r="2.5"/>
          <rect x="5" y="11" width="18" height="6" rx="1"/>
          <path d="M3 12v9h5M25 12v9h-5M10 17v9M18 17v9"/>
        </svg>
      </div>
      <p class="service__text">We'll provide easy to understand financial reports that allow you and your team to manage cash flow, create budgets and make forecasting decisions. Want real time data? Let us provide solutions with the latest in mobile apps and dashboards.</p>
    </article>
  </div>
</section>

<!-- BACK -->
<section class="postcard postcard--back" aria-label="Postcard back">
  <svg class="postcard__art" viewBox="0 0 796 536">
    <defs>
      <linearGradient id="backPanel" x1="0" y1="0" x2="0" y2="1">
        <stop offset="0" stop-color="var(--mid-blue)"/>
        <stop offset="0.55" stop-color="var(--bright-blue)"/>
        <stop offset="1" stop-color="var(--navy-deep)"/>
      </linearGradient>
    </defs>
    <polygon role="img" aria-label="Blue-tinted photo of a team of accountants at work, faded behind the text"
      points="0,0 311,0 402,300 306,536 0,536" fill="url(#backPanel)"/>
    <polygon points="344,0 356,0 414,300 408,300" fill="var(--mid-blue)"/>
    <polygon points="334,536 348,536 416,360 410,360" fill="var(--mid-blue)"/>
    <circle cx="409" cy="328" r="63" fill="var(--white)"/>
    <circle cx="409" cy="328" r="56" fill="none" stroke="var(--navy)" stroke-width="1.5"/>
    <circle cx="409" cy="328" r="41" fill="var(--brand-green)"/>
  </svg>

  <div class="brand">
    <span class="brand__mark"></span>
    <span class="brand__name">Pine Vale<br>Accounting</span>
  </div>

  <div class="message">
    <h1 class="message__title">Accounting for<br>your business</h1>
    <p class="message__lead">Specializing in cloud-based<br>bookkeeping &amp; payroll processing<br>with LedgerCloud Online by Numera.</p>
    <div class="vision">
      <h2 class="vision__title">Our Vision</h2>
      <p class="vision__text">At Pine Vale Accounting we have one mission in mind… to improve the quality, accuracy and efficiency of your business's back-end bookkeeping and payroll processing, so that you can focus on the nuts and bolts of your day to day operations.</p>
      <p class="vision__text">Founded by a former CFO in the San Francisco Bay Area, we bring a team of accounting professionals with over 20 years of expertise from one of the most competitive markets in the world.</p>
      <p class="vision__text">Our company grew from personal success in business financial management. We bring knowledge, insight and guidance to your business, offering value for time and money.</p>
      <p class="vision__text">From bookkeeping to financial reporting to payroll and beyond, we at Pine Vale Accounting have the expertise to provide your business with a comprehensive evaluation and easy to implement solutions.</p>
    </div>
  </div>

  <div class="contact">
    <p class="contact__label">CALL US ON</p>
    <p class="contact__phone">
      <svg viewBox="0 0 12 24" aria-hidden="true"><path d="M9 2C3 6 3 18 9 22l2-4c-3-2-3-10 0-12z" fill="var(--white)"/></svg>
      1.800.555.0142
    </p>
    <p class="contact__email">
      <svg viewBox="0 0 12 9" aria-hidden="true"><rect width="12" height="9" fill="var(--white)"/><path d="M0 0l6 5 6-5" fill="none" stroke="var(--navy)" stroke-width="1"/></svg>
      INFO@PINEVALEACCOUNTING.EXAMPLE
    </p>
  </div>

  <div class="social" aria-label="Social profiles">
    <span class="social__dot"></span>
    <span class="social__dot"></span>
  </div>

  <div class="stamp-box" aria-label="Stamp area"></div>
  <div class="address-line" style="top:204px"></div>
  <div class="address-line" style="top:278px"></div>
  <div class="address-line" style="top:349px"></div>
  <div class="address-line" style="top:426px"></div>
</section>

</body>
</html>
```